LUMETTE INC. is a new Fashion Stylist, Design Merchandiser, and consultant in the fashion industry

We need a logo design for a new Calgary, Alberta based company that is in the business of making over your image, wardrobe and style for both business and personal purposes.

Target Market(s)

Professional female and male business people looking for a new style or complete fashion makeover including clothes closet merchandising and makeover.

Contact Information for Business Card

see the uploaded file

Number of Pages Required

1 page

Font styles to use
Script

Colors
fac994
fbe7d2
fee3d4

Requirements
Must have
• Fashion Industry theme that is very elegant and colorful using gold/bronze/silver color themes.
Nice to have
• Incorporate the company name with the creative font to come up with the appropriate "logo"

```html
<!DOCTYPE html>
<html lang="en">
<head>
<meta charset="utf-8">
<title>Lumette Inc. – Business Card</title>
<link rel="stylesheet" href="https://fonts.googleapis.com/css2?family=Damion&family=Roboto:wght@700&display=swap">
<style>
  :root {
    --backdrop: #434343;
    --card-paper: #f3f3f3;
    --gold: #c99a2a;
    --gold-soft: #d4a93e;
  }
  * { margin: 0; padding: 0; box-sizing: border-box; }
  html, body {
    width: 1189px;
    height: 1200px;
    overflow: hidden;
    background: var(--backdrop);
  }
  .sheet {
    position: relative;
    width: 1189px;
    height: 1200px;
  }
  .card {
    position: absolute;
    left: 171px;
    width: 856px;
    height: 488px;
    border-radius: 22px;
    background: var(--card-paper);
  }
  .card--front { top: 67px; }
  .card--back  { top: 626px; }

  .brand {
    position: absolute;
    inset: 0;
    display: flex;
    align-items: center;
    justify-content: center;
  }
  .brand__name {
    font-family: "Roboto", sans-serif;
    font-weight: 700;
    font-size: 50px;
    letter-spacing: 4px;
    line-height: 1;
    color: var(--gold);
  }

  .contact {
    position: absolute;
    left: 0; right: 0;
    text-align: center;
    line-height: 1;
  }
  .contact__name {
    top: 168px;
    font-family: "Damion", cursive;
    font-size: 60px;
    color: var(--gold);
  }
  .contact__role {
    top: 238px;
    font-family: "Roboto", sans-serif;
    font-weight: 700;
    font-size: 21px;
    letter-spacing: 1.3px;
    color: var(--gold-soft);
  }
  .contact__phone {
    top: 311px;
    font-family: "Roboto", sans-serif;
    font-weight: 700;
    font-size: 28px;
    letter-spacing: 2.5px;
    color: var(--gold-soft);
  }
</style>
</head>
<body>
  <main class="sheet">
    <section class="card card--front" aria-label="Card front">
      <div class="brand">
        <p class="brand__name">LUMETTE INC.</p>
      </div>
    </section>

    <section class="card card--back" aria-label="Card back">
      <p class="contact contact__name">Marisol Verhoeven</p>
      <p class="contact contact__role">fashin stylist design merchandiser consultant</p>
      <p class="contact contact__phone">403-555-0142</p>
    </section>
  </main>
</body>
</html>
```